Cool modern, tech Business card design

Looking for a new business card design for our Managed IT Services company. We would like 2 sides, with the logo one one side horizontally and then the information on the back in either vertical or horizontal. We want our colors from the logo incorporated but also would like to see the color gray in there as well.

Target Market(s)

IT, Information Technology, Tech, Service

Industry/Entity Type

It Service

Contact Information for Business Card

Carl Penner
Managing Partner
(P)555-271-4830 ext xxx
(F)555-271-4831
www.brixtelcore.com

Font styles to use
Sans Serif

Colors
959595
000000
ec1f27

Requirements
Must have
• Logo on one side with some nice design or pattern
• Information on back in either vertical or horizontal format
Nice to have
• For it to look cool, tech, modern, stand out.

```html
<!DOCTYPE html>
<html lang="en">
<head>
<meta charset="utf-8">
<title>Brixtelcore Business Card</title>
<link href="https://fonts.googleapis.com/css2?family=Open+Sans:wght@400;600&display=swap" rel="stylesheet">
<style>
  :root {
    --red: #ec1f27;
    --red-dark: #b5141b;
    --black: #000000;
    --gray: #959595;
    --white: #ffffff;
    --stage: #3a3d40;
  }
  * { box-sizing: border-box; margin: 0; padding: 0; }
  html, body { width: 1200px; height: 807px; overflow: hidden; }
  body {
    background: var(--stage);
    font-family: "Open Sans", Arial, sans-serif;
    position: relative;
  }
  .card {
    position: absolute;
    top: 255px;
    width: 520px;
    height: 297px;
    border-radius: 14px;
    background: var(--red);
    overflow: hidden;
  }
  .card--back { left: 50px; }
  .card--front { left: 630px; }
  .card__panel {
    position: absolute;
    top: 0; bottom: 0;
    left: 18px; right: 18px;
    background: linear-gradient(160deg, #161616 0%, var(--black) 60%);
  }
  .card__notch {
    position: absolute;
    width: 10px; height: 60px;
    background: var(--red-dark);
    border-radius: 0 4px 4px 0;
  }
  .card__notch--left { left: 18px; top: 40px; }
  .card__notch--right { right: 18px; bottom: 40px; border-radius: 4px 0 0 4px; }

  .brand {
    font-weight: 400;
    color: var(--white);
    letter-spacing: 1px;
    white-space: nowrap;
  }
  .brand--small { position: absolute; left: 46px; top: 40px; font-size: 20px; }

  .name-tab {
    position: absolute;
    left: 258px; right: 0;
    top: 78px;
    height: 72px;
    background: var(--red);
    border-radius: 10px 0 0 10px;
    padding: 10px 20px;
    color: var(--white);
  }
  .name-tab__name { font-size: 28px; font-weight: 600; line-height: 1.1; }
  .name-tab__title { font-size: 15px; line-height: 1.4; }

  .contacts {
    position: absolute;
    left: 262px; top: 164px;
    list-style: none;
  }
  .contacts li {
    display: flex; align-items: center; gap: 10px;
    color: var(--white);
    font-size: 13px;
    height: 21px;
    white-space: nowrap;
  }
  .icon {
    width: 14px; height: 14px;
    border-radius: 50%;
    background: var(--red);
    display: inline-flex; align-items: center; justify-content: center;
    flex: none;
  }
  .icon svg { width: 9px; height: 9px; fill: var(--white); }
  .site {
    position: absolute;
    display: flex; align-items: center; gap: 8px;
    color: var(--white);
    font-size: 13px;
    white-space: nowrap;
  }
  .card--back .site { left: 46px; bottom: 30px; }

  .front-brand {
    position: absolute;
    left: 110px; top: 112px;
    font-size: 40px;
  }
  .card--front .site { left: 112px; top: 182px; font-size: 12px; }
</style>
</head>
<body>

<section class="card card--back" aria-label="Card back">
  <div class="card__panel"></div>
  <div class="card__notch card__notch--left"></div>
  <div class="card__notch card__notch--right"></div>

  <div class="brand brand--small">Brixtelcore</div>

  <div class="name-tab">
    <div class="name-tab__name">Carl Penner</div>
    <div class="name-tab__title">Managing Partner</div>
  </div>

  <ul class="contacts">
    <li><span class="icon"><svg viewBox="0 0 10 10"><path d="M2 1l2 2-1 1c.6 1.2 1.6 2.2 3 3l1-1 2 2-1.5 1.5C4 9 1 6 .5 2.5z"/></svg></span>555-271-4830 ext xxx</li>
    <li><span class="icon"><svg viewBox="0 0 10 10"><rect x="1" y="3" width="8" height="5" rx="1"/><rect x="3" y="1" width="4" height="2"/></svg></span>555-271-4831</li>
    <li><span class="icon"><svg viewBox="0 0 10 10"><path d="M1 2h8v6H1z M1 2l4 3 4-3" stroke="#ec1f27" stroke-width=".8"/></svg></span>hello@brixtelcore.com</li>
  </ul>

  <div class="site"><span class="icon"><svg viewBox="0 0 10 10"><circle cx="5" cy="5" r="3.5"/></svg></span>www.brixtelcore.com</div>
</section>

<section class="card card--front" aria-label="Card front">
  <div class="card__panel"></div>
  <div class="card__notch card__notch--left"></div>
  <div class="card__notch card__notch--right"></div>

  <div class="brand front-brand">Brixtelcore</div>

  <div class="site"><span class="icon"><svg viewBox="0 0 10 10"><circle cx="5" cy="5" r="3.5"/></svg></span>www.brixtelcore.com</div>
</section>

</body>
</html>
```